Company brochure for our unique consulting business

We are a small consulting business offering a unique set of services to our clients.. In simple terms we are a business improvement consultancy helping our clients get the best out of their businesses. We work with clients across multiple sectors and deliver a variety of services. We want to put together a brochure to cover these main themes:1. Who we are2. What we do3. The type of people we employ4. The sectors we work inWhile the brochure needs to have a certain corporate feel to it, we don't want it to be "boring" or "stiff". We would like it to have a slightly "friendly" or "informal" feel to it, to reflect the type of organisation we are.We have a company website http://tollandvergeadvisory.com , however we do not want to directly replicate the content or feel as we recognise it needs updating.We would like the brochure to be A4 portrait format. We anticipate requiring 12 sides (including covers) but we are happy to be guided on this based on the content we have provided.The attached ppt file gives the detail of the content to be included and also shows the proposed pagination. For the front cover we would like to try 2 versions, one with the TVA logo and one with the Tolland Verge Advisory logo (a file of both is attached)One of the most important pages will be the "Our Services" page. We would like this to cover the centre fold. In the ppt file we have shown an example layout, but this is where we need most help - we are clearly not graphic designers! This page will be the most used page in sales meetings etc.Also attached is the following:1. file for our TollandVerge Advisory company logo.2. File for our TVA company logo3. Files for Derek's signatures (for under photos) - Owen's to follow4. Photo of Derek & Owen (person in purple shirt to be cropped out)Thank you and really excited to see what everyone comes back with.Derek & Owen

Target Market(s)

Very broad - Manufacturing, Healthcare, Hospitality

Industry/Entity Type

Management Consulting

Font styles to use
Other font styles liked:
• We use Swiss721, but happy to be guided by designer

Colors
3276b5
85abd2
0355a3
333333
5c5c5c
9d9d9d
d9d9d9

Requirements
Must have
• Corporate feel
Nice to have
• Slightly friendly feel
• Our standard "blue" is (CORRECTION) - R55 G96 B146 #376092 and our standard grey is R197 G178, B179 - #B3B2B2, which we would like to keep, but other colours we are happy to be guided on. Brand guidelines attached.

```html
<!DOCTYPE html>
<html lang="en">
<head>
<meta charset="utf-8">
<title>Tolland Verge Advisory – Brochure Cover Spread</title>
<link rel="stylesheet" href="https://fonts.googleapis.com/css2?family=Arimo:wght@400;500;600&family=PT+Sans&display=swap">
<style>
  :root {
    --board: #e1e3e6;
    --paper: #ffffff;
    --ink: #111111;
    --text-grey: #5c5c5c;
    --soft-grey: #9d9d9d;
    --band-grey: #b3b2b2;
    --light-grey: #d9d9d9;
    --blue: #0355a3;
    --blue-mid: #3276b5;
    --blue-light: #85abd2;
    --brand-blue: #376092;
    --resource: #b5762a;
    --leisure: #a3222a;
    --property: #4d9a2e;
  }
  * { margin: 0; padding: 0; box-sizing: border-box; }
  html, body { width: 1200px; height: 830px; overflow: hidden; background: var(--board); }
  body { font-family: "Arimo", Arial, sans-serif; color: var(--ink); position: relative; }

  .spread { position: absolute; left: 127px; top: 82px; width: 944px; height: 666px; background: var(--paper); }
  .spread-art { position: absolute; inset: 0; width: 944px; height: 666px; }

  .page { position: absolute; top: 0; width: 472px; height: 666px; }
  .page--back { left: 0; }
  .page--front { left: 472px; }

  .wordmark { position: absolute; font-weight: 600; color: var(--ink); line-height: 1; letter-spacing: -0.5px; }
  .page--back .wordmark { left: 304px; top: 550px; font-size: 18px; }
  .page--front .wordmark { right: 35px; top: 448px; font-size: 29px; text-align: right; }

  .contact { position: absolute; top: 616px; font-size: 9px; line-height: 1.45; color: var(--text-grey); font-style: normal; }
  .contact--address { right: 190px; text-align: right; }
  .contact--phone { left: 302px; }
  .contact-divider { position: absolute; left: 293px; top: 610px; width: 1px; height: 34px; background: var(--light-grey); }

  .tagline { position: absolute; left: 40px; top: 558px; font-size: 19px; color: var(--soft-grey); font-weight: 400; }
  .divisions { position: absolute; left: 40px; top: 586px; display: flex; gap: 18px; list-style: none; }
  .division { display: flex; flex-direction: column; align-items: flex-end; }
  .division-name { font-size: 13px; font-weight: 600; line-height: 1; color: var(--ink); }
  .division-sector { font-size: 7.5px; line-height: 1.3; }
  .division-sector--resource { color: var(--resource); }
  .division-sector--leisure { color: var(--leisure); }
  .division-sector--property { color: var(--property); }
  .web { position: absolute; left: 40px; top: 620px; font-size: 10.5px; color: var(--text-grey); }

  .caption { position: absolute; top: 766px; width: 472px; text-align: center; font-family: "PT Sans", Arial, sans-serif; font-size: 17px; color: #555555; }
  .caption--back { left: 127px; }
  .caption--front { left: 599px; }
</style>
</head>
<body>
  <main class="spread">
    <svg class="spread-art" viewBox="0 0 944 666" xmlns="http://www.w3.org/2000/svg">
      <defs>
        <linearGradient id="skyline-tone" x1="0" y1="0" x2="0" y2="1">
          <stop offset="0" stop-color="#ffffff"/>
          <stop offset="0.45" stop-color="#f4f4f4"/>
          <stop offset="1" stop-color="#dedede"/>
        </linearGradient>
        <linearGradient id="photo-tone" x1="0" y1="0" x2="1" y2="1">
          <stop offset="0" stop-color="#3e6faa"/>
          <stop offset="0.5" stop-color="#5f7ea6"/>
          <stop offset="0.75" stop-color="#8a95a8"/>
          <stop offset="1" stop-color="#b4c7dc"/>
        </linearGradient>
        <linearGradient id="band-blue" x1="0" y1="1" x2="1" y2="0">
          <stop offset="0" stop-color="#0d4fa0"/>
          <stop offset="1" stop-color="#3276b5"/>
        </linearGradient>
      </defs>

      <!-- back cover: skyline illustration area -->
      <path role="img" aria-label="Line drawing of a city skyline with tall office towers" fill="url(#skyline-tone)"
            d="M0 100 H330 V400 Q290 470 230 520 Q200 545 170 560 Q80 555 0 540 Z"/>
      <!-- back cover waves -->
      <path fill="var(--band-grey)" opacity="0.85" d="M0 530 Q90 556 185 548 Q120 580 0 582 Z"/>
      <path fill="url(#band-blue)"
            d="M0 580 Q110 582 190 548 Q270 505 330 425 Q400 330 472 298 V420 Q420 430 380 456 Q300 530 230 565 Q140 602 0 602 Z"/>
      <path fill="var(--blue-mid)" opacity="0.55" d="M340 420 Q400 335 472 302 V360 Q410 375 340 420 Z"/>

      <!-- front cover: blue band -->
      <path fill="url(#band-blue)"
            d="M472 468 Q610 470 700 412 Q800 340 944 158 V318 Q905 290 870 292 Q830 298 795 342 Q740 408 670 442 Q590 470 472 470 Z"/>
      <path fill="var(--blue-light)" opacity="0.6" d="M870 292 Q910 285 944 305 V318 Q910 292 870 292 Z"/>
      <!-- front cover: grey band under photo -->
      <path fill="var(--band-grey)"
            d="M472 360 V466 Q570 464 650 428 Q690 410 712 392 Q650 432 580 440 Q510 444 472 360 Z"/>
      <!-- front cover: photo area -->
      <path role="img" aria-label="Photograph of a business handshake over a city skyline at dusk" fill="url(#photo-tone)"
            stroke="#ffffff" stroke-width="3"
            d="M472 0 H944 V158 Q810 312 720 372 Q650 420 578 430 Q500 438 472 374 Z"/>
      <!-- front cover bottom corner -->
      <path fill="var(--band-grey)" d="M868 666 Q912 640 944 602 V666 Z"/>
      <path fill="var(--blue-mid)" d="M858 666 Q905 640 944 594 V604 Q910 645 872 666 Z"/>
    </svg>

    <section class="page page--back" aria-label="Back cover">
      <p class="wordmark">Tolland Verge<br>Advisory</p>
      <address class="contact contact--address">Millbrook House<br>Canal Lane | Harwick HW2 4QL | United Kingdom</address>
      <span class="contact-divider"></span>
      <p class="contact contact--phone">Tel: +44 (0)1632 960418<br>www.tollandvergeadvisory.com</p>
    </section>

    <section class="page page--front" aria-label="Front cover">
      <h1 class="wordmark">Tolland Verge<br>Advisory</h1>
      <p class="tagline">better people, better business</p>
      <ul class="divisions">
        <li class="division"><span class="division-name">Tolland Verge</span><span class="division-sector division-sector--resource">resource</span></li>
        <li class="division"><span class="division-name">Tolland Verge</span><span class="division-sector division-sector--leisure">leisure</span></li>
        <li class="division"><span class="division-name">Tolland Verge</span><span class="division-sector division-sector--property">property</span></li>
      </ul>
      <p class="web">www.tollandvergeadvisory.com</p>
    </section>
  </main>

  <p class="caption caption--back">Cover Back</p>
  <p class="caption caption--front">Cover Front</p>
</body>
</html>
```